Rock band business card design

I need an edgy double sided business card to hand out at music events and to send out to radio.

It needs to display our logo, web address and social media icons (linkora, plumbit, vostramesh).

Colour scheme to match our website (www.thedrelliq.com)

Please include this quote:
The clock is turning... a reckoning... THE DRELLIQ.

Logo files have been attached.

I look forward to seeing your designs!

Target Market(s)

radio stations, music fans.

Industry/Entity Type

Events

Requirements
Must have
• Website address, social media icons, quote, colour scheme to match www.thedrelliq.com

```html
<!DOCTYPE html>
<html lang="en">
<head>
<meta charset="utf-8">
<title>The Drelliq — Business Card</title>
<link rel="stylesheet" href="https://fonts.googleapis.com/css2?family=Aladin&family=Metamorphous&display=swap">
<style>
  :root {
    --page: #ffffff;
    --card-front: #eeea8e;
    --card-front-grain: #e6e180;
    --card-back: #000000;
    --ink-dark: #111111;
    --ink-light: #ffffff;
    --art-top: #2a2a22;
    --art-bottom: #6d6a45;
  }
  * { margin: 0; padding: 0; box-sizing: border-box; }
  html, body { width: 1200px; height: 1119px; overflow: hidden; background: var(--page); }
  .canvas { position: relative; width: 1200px; height: 1119px; }

  .card { position: absolute; left: 106px; width: 765px; height: 466px; }
  .card--front {
    top: 108px;
    background: repeating-linear-gradient(0deg, var(--card-front) 0 2px, var(--card-front-grain) 2px 3px);
    color: var(--ink-dark);
  }
  .card--back { top: 648px; background: var(--card-back); color: var(--ink-light); }

  .band-name {
    position: absolute; left: 0; right: 0; text-align: center;
    font-family: "Aladin", "Metamorphous", serif; font-weight: 400;
  }
  .card--front .band-name { top: 34px; font-size: 42px; }
  .card--back .band-name { top: 18px; font-size: 60px; }

  .logo-art {
    position: absolute; left: 256px; top: 93px; width: 242px; height: 227px;
    background: linear-gradient(180deg, var(--art-top), var(--art-bottom));
  }

  .quote {
    position: absolute; left: 0; right: 0; top: 365px; text-align: center;
    font-family: "Metamorphous", serif; font-size: 20px; line-height: 30px;
    text-transform: uppercase; letter-spacing: 0.5px;
  }

  .website {
    position: absolute; left: 0; right: 0; top: 124px; text-align: center;
    font-family: "Metamorphous", serif; font-size: 20px; letter-spacing: 1px;
    text-transform: uppercase;
  }

  .social { position: absolute; left: 0; top: 0; width: 100%; height: 100%; list-style: none; }
  .social__item { position: absolute; left: 130px; display: flex; align-items: center; }
  .social__item:nth-child(1) { top: 184px; }
  .social__item:nth-child(2) { top: 273px; }
  .social__item:nth-child(3) { top: 367px; }
  .social__mark {
    width: 96px; text-align: center;
    font-family: "Metamorphous", serif; font-size: 14px;
  }
  .social__link {
    margin-left: 4px;
    font-family: "Metamorphous", serif; font-size: 17px; letter-spacing: 0.5px;
    text-transform: uppercase;
  }

  .side-label {
    position: absolute; font-family: "Aladin", serif; font-size: 46px;
    color: var(--ink-dark); letter-spacing: 2px;
  }
  .side-label--front { left: 1010px; top: 312px; }
  .side-label--back { left: 1022px; top: 852px; }
</style>
</head>
<body>
<main class="canvas">
  <section class="card card--front">
    <h1 class="band-name">THE DRELLIQ</h1>
    <div class="logo-art" role="img" aria-label="Band emblem illustration: dark triangle artwork"></div>
    <p class="quote">The clock is turning.<br>A reckoning.<br>The Drelliq.</p>
  </section>

  <section class="card card--back">
    <h2 class="band-name">THE DRELLIQ</h2>
    <p class="website">www.thedrelliq.com</p>
    <ul class="social">
      <li class="social__item"><span class="social__mark">plumbit</span><span class="social__link">https://plumbit.com/thedrelliq</span></li>
      <li class="social__item"><span class="social__mark">linkora</span><span class="social__link">https://www.linkora.com/thedrelliq</span></li>
      <li class="social__item"><span class="social__mark">vostramesh</span><span class="social__link">http://www.vostramesh.com/thedrelliq</span></li>
    </ul>
  </section>

  <span class="side-label side-label--front">FRONT</span>
  <span class="side-label side-label--back">BACK</span>
</main>
</body>
</html>
```